" Somos uma empresa afiliada a Corvane Capital e representamos ela em Cuiabá. Prestamos o serviço de assessoria em investimentos a clientes de alto poder aquisitivo, um público private. Serviço exclusivo de "

```html
<!DOCTYPE html>
<html lang="pt-BR">
<head>
<meta charset="UTF-8">
<title>Veltra Investimentos — Cartão de visita</title>
<link rel="stylesheet" href="https://fonts.googleapis.com/css2?family=Cinzel:wght@500;600&family=Montserrat:wght@400;500;700&display=swap">
<style>
  :root {
    --page-bg: #e4e5e8;
    --navy-deep: #07112a;
    --navy-mid: #13285a;
    --navy-glow: #1f3c7a;
    --gold: #c9a45c;
    --gold-light: #ecd49a;
    --paper: #fbfbfc;
    --ink: #1c2438;
    --ink-soft: #5a6275;
  }
  * { box-sizing: border-box; margin: 0; padding: 0; }
  html, body { width: 1200px; height: 1200px; overflow: hidden; }
  body {
    background: var(--page-bg);
    font-family: "Montserrat", sans-serif;
    display: flex;
    flex-direction: column;
    align-items: center;
    justify-content: center;
    gap: 60px;
  }
  .card {
    position: relative;
    width: 900px;
    height: 500px;
    border-radius: 26px;
    overflow: hidden;
    box-shadow: 0 10px 30px rgba(0,0,0,0.18);
  }

  /* Front */
  .card--front {
    background: radial-gradient(ellipse at 55% 45%, var(--navy-glow) 0%, var(--navy-mid) 40%, var(--navy-deep) 100%);
  }
  .front-rule {
    position: absolute;
    left: 30px; top: 0; bottom: 0;
    width: 4px;
    background: linear-gradient(180deg, var(--gold-light), var(--gold), var(--gold-light));
  }
  .front-edge {
    position: absolute;
    left: 0; top: 0; bottom: 0;
    width: 10px;
    background: linear-gradient(180deg, var(--gold), var(--gold-light), var(--gold));
    opacity: 0.85;
  }
  .front-brand {
    position: absolute;
    inset: 0;
    display: flex;
    flex-direction: column;
    align-items: center;
    justify-content: center;
    color: var(--gold-light);
  }
  .front-brand .brand-name {
    font-family: "Cinzel", serif;
    font-weight: 500;
    font-size: 104px;
    letter-spacing: 6px;
    line-height: 1;
  }
  .front-brand .brand-sub {
    font-family: "Cinzel", serif;
    font-weight: 500;
    font-size: 24px;
    letter-spacing: 11px;
    margin-top: 14px;
  }

  /* Back */
  .card--back { background: var(--paper); }
  .back-divider {
    position: absolute;
    left: 470px; top: 0; bottom: 0;
    width: 3px;
    background: linear-gradient(180deg, var(--gold-light), var(--gold), var(--gold-light));
  }
  .back-bottom-rule {
    position: absolute;
    left: 0; right: 0; bottom: 0;
    height: 6px;
    background: linear-gradient(90deg, var(--gold), var(--gold-light), var(--gold));
  }
  .back-brand {
    position: absolute;
    left: 70px; top: 120px;
    color: var(--ink);
  }
  .back-brand .brand-name {
    font-family: "Cinzel", serif;
    font-weight: 600;
    font-size: 66px;
    letter-spacing: 4px;
    line-height: 1;
  }
  .back-brand .brand-sub {
    font-family: "Cinzel", serif;
    font-weight: 600;
    font-size: 16px;
    letter-spacing: 7px;
    margin-top: 10px;
  }
  .partner {
    position: absolute;
    left: 70px; top: 300px;
    width: 370px;
    display: flex;
    align-items: center;
    gap: 16px;
  }
  .partner-badge {
    flex: none;
    width: 46px; height: 46px;
    background: var(--ink);
  }
  .partner-text {
    font-size: 12px;
    line-height: 1.5;
    color: var(--ink-soft);
    text-transform: uppercase;
    letter-spacing: 0.5px;
  }
  .contact {
    position: absolute;
    left: 515px; top: 110px;
    color: var(--ink);
  }
  .contact .person-name {
    font-size: 30px;
    font-weight: 400;
    letter-spacing: 2px;
  }
  .contact .person-role {
    font-size: 19px;
    font-weight: 700;
    margin-top: 4px;
  }
  .contact-list {
    list-style: none;
    margin-top: 34px;
    display: flex;
    flex-direction: column;
    gap: 16px;
  }
  .contact-list li {
    display: flex;
    align-items: flex-start;
    gap: 14px;
    font-size: 16px;
    line-height: 1.35;
    color: var(--ink-soft);
  }
  .contact-icon {
    flex: none;
    width: 28px; height: 28px;
    border-radius: 50%;
    background: var(--ink);
    display: flex;
    align-items: center;
    justify-content: center;
  }
</style>
</head>
<body>

  <section class="card card--front" aria-label="Frente do cartão">
    <div class="front-edge"></div>
    <div class="front-rule"></div>
    <div class="front-brand">
      <span class="brand-name">VELTRA</span>
      <span class="brand-sub">INVESTIMENTOS</span>
    </div>
  </section>

  <section class="card card--back" aria-label="Verso do cartão">
    <div class="back-brand">
      <div class="brand-name">VELTRA</div>
      <div class="brand-sub">INVESTIMENTOS</div>
    </div>

    <div class="partner">
      <div class="partner-badge"></div>
      <p class="partner-text">Assessor autônomo de investimentos<br>vinculado à Corvane Capital</p>
    </div>

    <div class="back-divider"></div>

    <div class="contact">
      <div class="person-name">NOME COMPLETO</div>
      <div class="person-role">Cargo</div>
      <ul class="contact-list">
        <li>
          <span class="contact-icon">
            <svg width="14" height="14" viewBox="0 0 24 24" fill="#ffffff"><path d="M6.6 10.8a15.1 15.1 0 0 0 6.6 6.6l2.2-2.2a1 1 0 0 1 1-.25 11.4 11.4 0 0 0 3.6.57 1 1 0 0 1 1 1V20a1 1 0 0 1-1 1A17 17 0 0 1 3 4a1 1 0 0 1 1-1h3.5a1 1 0 0 1 1 1c0 1.25.2 2.45.57 3.57a1 1 0 0 1-.25 1z"/></svg>
          </span>
          <span>(00) 0000-0000</span>
        </li>
        <li>
          <span class="contact-icon">
            <svg width="14" height="14" viewBox="0 0 24 24" fill="#ffffff"><path d="M12 2a7 7 0 0 0-7 7c0 5.25 7 13 7 13s7-7.75 7-13a7 7 0 0 0-7-7zm0 9.5A2.5 2.5 0 1 1 12 6.5a2.5 2.5 0 0 1 0 5z"/></svg>
          </span>
          <span>Seu endereço - Bairro<br>Cidade - Estado<br>CEP 0000-0000</span>
        </li>
        <li>
          <span class="contact-icon">
            <svg width="14" height="14" viewBox="0 0 24 24" fill="#ffffff"><path d="M3 5h18v14H3zm2 2v.5l7 4.5 7-4.5V7l-7 4.5z"/></svg>
          </span>
          <span>seuemail@exemplo.com</span>
        </li>
      </ul>
    </div>

    <div class="back-bottom-rule"></div>
  </section>

</body>
</html>
```